Full Page Ad

We are like looking for something modern, Rustic and unique for a full page ad that includes our logo, office locations, contact information. Please see our webpage and www.BRINKClaimsworks.com. I can send our logo as well.
Updates

Looking for something elegant but industrial, rustic and modern. Added Sunday, June 4, 2017

Industry/Entity Type

Insurance

Font styles to use
Serif

Requirements
Must have
• Contact information

```html
<!DOCTYPE html>
<html lang="en">
<head>
<meta charset="utf-8">
<title>BRINK Claimsworks – Full Page Ad</title>
<link rel="stylesheet" href="https://fonts.googleapis.com/css2?family=Archivo+Black&family=Open+Sans:wght@300;400&family=Oswald:wght@600&family=Signika:wght@400;600&display=swap">
<style>
  :root{
    --orange:#f0813a;
    --white:#ffffff;
    --stone-light:#8c8d8b;
    --stone-dark:#5f615f;
    --band:#2b1810;
    --wood-light:#a5561f;
    --wood-dark:#6a3213;
  }
  *{margin:0;padding:0;box-sizing:border-box}
  html,body{width:1200px;height:1085px;overflow:hidden;background:var(--wood-dark)}
  .ad{position:relative;width:1200px;height:1085px;overflow:hidden;font-family:"Open Sans",sans-serif;color:var(--white)}
  .surface-stone{position:absolute;left:0;top:0;width:1200px;height:531px;
    background:radial-gradient(ellipse at 50% 40%,var(--stone-light) 0%,#7a7b79 55%,var(--stone-dark) 100%)}
  .surface-wood{position:absolute;left:0;top:531px;width:1200px;height:554px;
    background:radial-gradient(ellipse at 50% 35%,var(--wood-light) 0%,#8a4419 55%,var(--wood-dark) 100%)}
  .locations{position:absolute;left:0;top:531px;width:1200px;height:83px;background:var(--band);opacity:.93;
    display:flex;flex-direction:column;justify-content:center;align-items:center;gap:4px;
    font-family:"Oswald",sans-serif;font-weight:600;font-size:21px;letter-spacing:.3px;text-transform:uppercase}
  .locations p{white-space:nowrap}
  .locations .sep{color:var(--orange);margin:0 7px}
  .brand-name{position:absolute;left:0;top:248px;width:1200px;text-align:center;
    font-family:"Archivo Black",sans-serif;font-size:250px;line-height:1;color:var(--orange);letter-spacing:-4px}
  .brand-full{position:absolute;left:0;top:466px;width:1200px;text-align:center;
    font-weight:300;font-size:38px;letter-spacing:.5px;text-transform:uppercase}
  .tagline{position:absolute;left:0;top:798px;width:1200px;text-align:center;
    font-family:"Signika",sans-serif;font-size:36px;letter-spacing:.6px}
  .phone{position:absolute;left:0;top:852px;width:1200px;text-align:center;
    font-family:"Signika",sans-serif;font-weight:600;font-size:37px;color:var(--orange);letter-spacing:.5px}
  .website{position:absolute;left:0;top:1048px;width:1200px;text-align:center;font-size:22px}
</style>
</head>
<body>
<main class="ad">
  <div class="surface-stone" role="img" aria-label="Weathered grey wood plank texture"></div>
  <div class="surface-wood" role="img" aria-label="Rustic stained brown wood texture"></div>

  <h1 class="brand-name">BRINK</h1>
  <p class="brand-full">Brink Claimsworks Adjusting Services</p>

  <div class="locations">
    <p>Albany, NY<span class="sep">•</span>Utica, NY<span class="sep">•</span>Plattsburgh, NY<span class="sep">•</span>Poughkeepsie, NY<span class="sep">•</span>Queensbury, NY<span class="sep">•</span>Rochester, NY</p>
    <p>Syracuse, NY<span class="sep">•</span>Watertown, NY<span class="sep">•</span>Elmira, NY<span class="sep">•</span>Buffalo, NY<span class="sep">•</span>Long Island, NY<span class="sep">•</span>Springfield, MA</p>
  </div>

  <p class="tagline">Timely, commited, empathetic. Touch base with us today:</p>
  <p class="phone">1-800-555-0147</p>
  <p class="website">www.brinkclaimsworks.com</p>
</main>
</body>
</html>
```